Veltrano Strom GmbH webpage The online Business card of a master electrician

A clean, modern webpage on whitch i can show my clients what im capable of and where the future costumer can inform himself. I need a login page for costumers who are registred and an secound webpage where my stuff can login to report theyr labour.
I will post pictures before and after, put on some commercial and crossellimg informations.
The costumer should find my insta as well my twitter or snapchat accounts.

Update:
Our Services are, Installations, Renovations, Home Automation, CCTV, Telefon / VOIP, Networking / Network-Cabeling, Electrical Supervisioning

Target Market(s)

Private and business costumers

Industry/Entity Type

Electric Company

Number of Pages Required

5+ page

Font styles to use
Sans Serif
Other font styles liked:
• Zurich,

Colors

Designer to choose colors to be used in the design.

Requirements
Must have
• A Page Hero
• A Costumer and staff login page (2separate pages)
• Contact form
• Responsive form
• Instagram enbedding account veltrano_strom
Nice to have
• A Blog

```html
<!DOCTYPE html>
<html lang="en">
<head>
<meta charset="utf-8">
<title>Veltrano Strom – Electrician</title>
<link href="https://fonts.googleapis.com/css2?family=Exo+2:wght@600;700;800&family=Lato:wght@400;700;900&display=swap" rel="stylesheet">
<style>
:root{
  --blue:#0b5fbf;
  --blue-dark:#084a96;
  --ink:#1c1c1c;
  --text:#444;
  --muted:#777;
  --grey-bg:#efefed;
  --line:#cfcfcf;
  --footer:#1b2027;
  --white:#fff;
  --social-1:#f2d100;
  --social-2:#1d8fd6;
  --social-3:#d8336f;
}
*{box-sizing:border-box;margin:0;padding:0}
html,body{width:1200px;height:3797px;overflow:hidden}
body{position:relative;font-family:"Lato",sans-serif;color:var(--text);background:var(--white)}
.abs{position:absolute}
.heading{font-family:"Exo 2",sans-serif;font-weight:700;font-size:38px;color:var(--ink);text-align:center;letter-spacing:1px;text-transform:uppercase;width:100%;left:0}
.heading span{color:var(--blue)}
.heading-rule{left:450px;width:300px;height:1px;background:var(--line)}
.bolt-btn{display:flex;align-items:center;justify-content:center;background:var(--blue);color:var(--white);font:900 13px "Lato",sans-serif;letter-spacing:1px;height:36px;width:160px;left:520px;transform:skewX(-25deg)}
.bolt-btn b{transform:skewX(25deg)}

/* header */
.hero{left:0;top:84px;width:1200px;height:587px;background:linear-gradient(160deg,#3a3428 0%,#1f1f1e 45%,#2a2722 70%,#141414 100%)}
.hero-caption{left:0;top:590px;width:1200px;height:81px;background:rgba(0,0,0,.55)}
.hero-title{left:0;top:602px;width:1200px;text-align:center;font:700 36px "Exo 2",sans-serif;color:var(--white);letter-spacing:2px}
.hero-arrow{top:368px;width:58px;height:46px;background:var(--white);display:flex;align-items:center;justify-content:center}
.topbar{left:0;top:0;width:1200px;height:84px;background:var(--white)}
.logo-panel{left:0;top:0;width:480px;height:122px;background:var(--white);clip-path:polygon(0 0,100% 0,93% 100%,0 100%)}
.brand{left:100px;top:28px;display:flex;align-items:center;gap:14px;font:800 36px "Exo 2",sans-serif;color:var(--blue)}
.brand i{display:block;width:30px;height:30px;background:var(--blue)}
.call{left:672px;top:18px;display:flex;gap:10px;align-items:center;font-size:15px;color:var(--ink);line-height:1.2}
.login{top:20px;height:36px;background:var(--blue);color:var(--white);font:900 13px "Lato",sans-serif;display:flex;align-items:center;justify-content:center}
.nav{left:468px;top:84px;width:732px;height:36px;background:var(--blue);display:flex;align-items:center;padding-left:20px}
.nav a{color:var(--white);font:700 13px "Lato",sans-serif;text-decoration:none;padding:0 28px;height:36px;display:flex;align-items:center}
.nav a.active{background:var(--blue-dark)}

/* about */
.about-lead{left:110px;top:793px;width:980px;text-align:center;font:700 15px/1.6 "Lato",sans-serif;color:var(--ink)}
.about-body{left:100px;top:846px;width:1000px;text-align:center;font-size:13.5px;line-height:1.9;color:var(--text)}

/* services */
.services{left:0;top:1040px;width:1200px;height:649px;background:var(--grey-bg)}
.svc-label{font:700 16px "Exo 2",sans-serif;color:var(--ink);line-height:1.3}

/* gallery */
.photo{top:1823px;width:233px;height:233px;border:4px solid var(--blue)}

/* why */
.why{left:0;top:2183px;width:1200px;height:476px;background:var(--grey-bg)}
.video{left:99px;top:2324px;width:463px;height:279px;background:linear-gradient(135deg,#c6c2bd,#8c847a 45%,#3f3a35);}
.video-bar{left:99px;top:2577px;width:463px;height:26px;background:#1e1e1e}
.feature{left:608px;width:500px;display:flex;gap:26px}
.feature-icon{width:70px;height:70px;background:var(--blue);display:flex;align-items:center;justify-content:center;flex:none}
.feature h3{font:700 18px "Exo 2",sans-serif;color:var(--blue);margin:2px 0 6px}
.feature p{font-size:13px;line-height:1.6;color:var(--text)}

/* blog */
.post{top:2795px;width:312px}
.post-img{width:312px;height:172px}
.post-date{position:absolute;left:0;top:0;width:48px;height:58px;background:var(--blue);color:var(--white);text-align:center;font:900 22px/1 "Lato",sans-serif;padding-top:6px}
.post-date small{display:block;font:700 9px/1.2 "Lato",sans-serif;margin-top:2px}
.post h4{font:900 15px/1.4 "Lato",sans-serif;color:var(--ink);margin-top:20px}
.post .meta{font-size:11px;color:var(--muted);margin:10px 0 8px;display:flex;gap:12px;align-items:center}
.post .meta i{display:inline-block;width:10px;height:10px;background:var(--blue);border-radius:50%;margin-right:4px;vertical-align:-1px}
.post p{font-size:12px;line-height:1.55;color:var(--text)}
.side-arrow{top:2930px}

/* message */
.message{left:0;top:3157px;width:1200px;height:281px;background:var(--blue)}
.msg-title{left:101px;top:3205px;font:700 36px/1.2 "Exo 2",sans-serif;color:var(--white);letter-spacing:2px}
.msg-text{left:101px;top:3302px;width:300px;font-size:12px;line-height:1.6;color:#dbe7f6}
.form-label{left:458px;top:3210px;font-size:14px;color:var(--white)}
.field{height:41px;background:var(--white);font-size:12px;color:#555;padding:0 12px;display:flex;align-items:center;width:307px}
.submit{left:458px;top:3347px;width:162px;height:41px;background:#111;color:var(--white);font:900 15px "Lato",sans-serif;display:flex;align-items:center;justify-content:center;letter-spacing:1px}

/* footer */
.footer{left:0;top:3438px;width:1200px;height:284px;background:var(--footer)}
.contact-item{top:3480px;width:320px;text-align:center;color:var(--white);font-size:14px}
.contact-item svg{display:block;margin:0 auto 18px}
.foot-line{top:3500px;height:1px;background:#555}
.foot-text{left:300px;top:3592px;width:600px;text-align:center;font-size:12.5px;line-height:1.7;color:#ccc}
.foot-btn{left:540px;top:3660px;width:120px;height:32px;border:1px solid var(--white);color:var(--white);font:700 12px "Lato",sans-serif;display:flex;align-items:center;justify-content:center;letter-spacing:1px}
.copyright{left:101px;top:3751px;font-size:13px;color:var(--ink)}
.social{top:3738px;width:38px;height:38px;border-radius:50%}
</style>
</head>
<body>

<!-- header & hero -->
<div class="abs hero" role="img" aria-label="Restaurant interior with pendant lamps, a commercial electrical installation"></div>
<div class="abs hero-caption"></div>
<div class="abs hero-title">WE SPECIALIZED IN COMMERCIAL ELECTRICIAN</div>
<div class="abs hero-arrow" style="left:0"><svg width="14" height="20" viewBox="0 0 14 20"><path d="M11 2 3 10l8 8" fill="none" stroke="#111" stroke-width="3"/></svg></div>
<div class="abs hero-arrow" style="left:1142px"><svg width="14" height="20" viewBox="0 0 14 20"><path d="M3 2l8 8-8 8" fill="none" stroke="#111" stroke-width="3"/></svg></div>

<div class="abs topbar"></div>
<div class="abs logo-panel"></div>
<div class="abs brand"><i></i>Veltrano Strom</div>
<div class="abs call">
  <svg width="22" height="22" viewBox="0 0 24 24"><path d="M6.6 10.8a15 15 0 0 0 6.6 6.6l2.2-2.2c.3-.3.7-.4 1-.2 1.1.4 2.3.6 3.6.6.6 0 1 .4 1 1V20c0 .6-.4 1-1 1A17 17 0 0 1 3 4c0-.6.4-1 1-1h3.5c.6 0 1 .4 1 1 0 1.3.2 2.5.6 3.6.1.3 0 .7-.2 1z" fill="#1c1c1c"/></svg>
  <div>Call Us:<br><span style="font-size:13px">555-014-2270</span></div>
</div>
<div class="abs login" style="left:822px;width:144px">COSTUMER LOGIN</div>
<div class="abs login" style="left:984px;width:116px">STAFF LOGIN</div>
<nav class="abs nav">
  <a class="active">Home</a><a>About Us</a><a>Our Services</a><a>Photo Gallery</a><a>Contact Us</a>
</nav>

<!-- about -->
<h2 class="abs heading" style="top:712px">About <span>Us</span></h2>
<div class="abs heading-rule" style="top:762px"></div>
<p class="abs about-lead">Sed ut perspiciatis unde omnis iste natus error sit voluptatem accusantium doloremq laudantium, totam rem aperiam, eaque ipsa quae ab illo inventore Sed ut perspiciatis unde omnis iste natus error sit voluptatem accusantium doloremq.</p>
<p class="abs about-body">Lorem Ipsum is simply dummy text of the printing and typesetting industry. Lorem Ipsum has been the industry's standard dummy text ever since the 1500s, when an unknown printer took a galley of type and scrambled it to make a type specimen book. It has survived not only five centuries, but also the leap into electronic typesetting, remaining essentially unchanged.</p>
<div class="abs bolt-btn" style="top:952px"><b>READ MORE</b></div>

<!-- services -->
<div class="abs services"></div>
<h2 class="abs heading" style="top:1082px">Our <span>Services</span></h2>
<div class="abs heading-rule" style="top:1132px"></div>
<svg class="abs" style="left:0;top:1040px" width="1200" height="649" viewBox="0 1040 1200 649">
  <g stroke="#888" stroke-width="1.5" fill="#888">
    <line x1="656" y1="1222" x2="770" y2="1207"/><circle cx="770" cy="1207" r="3"/>
    <line x1="793" y1="1293" x2="900" y2="1293"/><circle cx="900" cy="1293" r="3"/>
    <line x1="831" y1="1442" x2="925" y2="1442"/><circle cx="925" cy="1442" r="3"/>
    <line x1="732" y1="1568" x2="845" y2="1568"/><circle cx="845" cy="1568" r="3"/>
    <line x1="468" y1="1568" x2="365" y2="1548"/><circle cx="365" cy="1548" r="3"/>
    <line x1="372" y1="1442" x2="282" y2="1442"/><circle cx="282" cy="1442" r="3"/>
    <line x1="405" y1="1293" x2="302" y2="1293"/><circle cx="302" cy="1293" r="3"/>
  </g>
  <g fill="#fff" stroke="var(--blue)" stroke-width="4">
    <circle cx="600" cy="1367" r="71"/>
    <circle cx="600" cy="1241" r="56"/>
    <circle cx="737" cy="1309" r="56"/>
    <circle cx="775" cy="1458" r="56"/>
    <circle cx="676" cy="1577" r="56"/>
    <circle cx="524" cy="1577" r="56"/>
    <circle cx="428" cy="1458" r="56"/>
    <circle cx="461" cy="1309" r="56" fill="var(--blue)"/>
  </g>
  <circle cx="461" cy="1309" r="62" fill="none" stroke="var(--blue)" stroke-width="1.5"/>
  <circle cx="600" cy="1367" r="18" fill="var(--blue)"/>
  <g fill="var(--blue)">
    <circle cx="600" cy="1241" r="38"/><circle cx="737" cy="1309" r="38"/><circle cx="775" cy="1458" r="38"/>
    <circle cx="676" cy="1577" r="38"/><circle cx="524" cy="1577" r="38"/><circle cx="428" cy="1458" r="38"/>
  </g>
  <g fill="none" stroke="#fff" stroke-width="4" stroke-linecap="round" stroke-linejoin="round">
    <path d="M584 1225l32 32M616 1225l-32 32"/>
    <path d="M717 1313l20-18 20 18M723 1308v18h28v-18"/>
    <path d="M443 1313l18-16 18 16M449 1308v18h24v-18"/>
    <path d="M757 1452h28v14h-28zM785 1459l12-6v12z"/>
    <path d="M664 1565h24v24h-24zM670 1577h12"/>
    <path d="M510 1590l26-26M512 1568l10 10"/>
    <path d="M418 1444v10M438 1444v10M412 1454h32v8a16 16 0 0 1-32 0z"/>
  </g>
</svg>
<div class="abs svc-label" style="left:780px;top:1197px">Installations</div>
<div class="abs svc-label" style="left:912px;top:1283px">Renovations</div>
<div class="abs svc-label" style="left:938px;top:1432px">CCTV</div>
<div class="abs svc-label" style="left:856px;top:1558px">Telefon / VOIP</div>
<div class="abs svc-label" style="left:155px;top:1530px;width:200px;text-align:right">Networking /<br>Network-Cabeling</div>
<div class="abs svc-label" style="left:60px;top:1420px;width:200px;text-align:right">Electrical<br>Supervisioning</div>
<div class="abs svc-label" style="left:108px;top:1283px;color:var(--blue)">Home Automation</div>

<!-- gallery -->
<h2 class="abs heading" style="top:1730px">Photo <span>Gallery</span></h2>
<div class="abs heading-rule" style="top:1780px"></div>
<div class="abs photo" style="left:101px;background:linear-gradient(160deg,#d9c8a8,#a88c62 55%,#2a2a2a)" role="img" aria-label="Boxed electrical components on a table"></div>
<div class="abs photo" style="left:357px;background:linear-gradient(160deg,#6d6a60,#b3ae9f 50%,#4a463e)" role="img" aria-label="Open distribution board with breakers"></div>
<div class="abs photo" style="left:613px;background:linear-gradient(160deg,#d8d4cc,#8e8a82 50%,#5a564e)" role="img" aria-label="Wiring work inside a panel"></div>
<div class="abs photo" style="left:868px;background:linear-gradient(160deg,#3c3a36,#e6e4e0 55%,#bcb8b0)" role="img" aria-label="Coffee cup on a saucer"></div>
<svg class="abs" style="left:50px;top:1925px" width="16" height="34"><path d="M14 2 3 17l11 15" fill="none" stroke="#ccc" stroke-width="2"/></svg>
<svg class="abs" style="left:1134px;top:1925px" width="16" height="34"><path d="M2 2l11 15L2 32" fill="none" stroke="#ccc" stroke-width="2"/></svg>
<div class="abs bolt-btn" style="top:2091px;width:140px;left:530px"><b>VIEW ALL</b></div>

<!-- why choose us -->
<div class="abs why"></div>
<h2 class="abs heading" style="top:2224px">Why <span>Choose Us</span></h2>
<div class="abs heading-rule" style="top:2274px"></div>
<div class="abs video" role="img" aria-label="Video still of an electrician mounting a security camera"></div>
<div class="abs video-bar"></div>
<svg class="abs" style="left:112px;top:2584px" width="440" height="12"><path d="M0 0l9 6-9 6z" fill="#ddd"/><rect x="24" y="5" width="400" height="2" fill="#666"/></svg>
<div class="abs feature" style="top:2342px"><div class="feature-icon"><svg width="34" height="34" viewBox="0 0 34 34" fill="#fff"><circle cx="17" cy="10" r="6"/><path d="M6 30c0-7 5-11 11-11s11 4 11 11z"/></svg></div><div><h3>Years Of Experience</h3><p>Lorem ipsum dolor sit amet, consectetuer adipiscing elit, sed diam nonummy nibh euismod.</p></div></div>
<div class="abs feature" style="top:2443px"><div class="feature-icon"><svg width="38" height="34" viewBox="0 0 38 34" fill="#fff"><circle cx="10" cy="11" r="5"/><circle cx="28" cy="11" r="5"/><path d="M1 30c0-6 4-10 9-10s9 4 9 10zM19 30c0-6 4-10 9-10s9 4 9 10z"/></svg></div><div><h3>Certified Experts</h3><p>Lorem ipsum dolor sit amet, consectetuer adipiscing elit, sed diam nonummy nibh euismod.</p></div></div>
<div class="abs feature" style="top:2544px"><div class="feature-icon"><svg width="34" height="34" viewBox="0 0 34 34" fill="none" stroke="#fff" stroke-width="3"><circle cx="17" cy="13" r="9"/><path d="M11 21l-3 11 9-4 9 4-3-11"/></svg></div><div><h3>Award Winning Services</h3><p>Lorem ipsum dolor sit amet, consectetuer adipiscing elit, sed diam nonummy nibh euismod.</p></div></div>

<!-- blog -->
<h2 class="abs heading" style="top:2700px">Latest <span>Blog</span></h2>
<div class="abs heading-rule" style="top:2750px"></div>
<article class="abs post" style="left:101px">
  <div style="position:relative"><div class="post-img" style="background:linear-gradient(150deg,#e9e6df,#b9b4aa 60%,#8a857b)" role="img" aria-label="Electrical plans with pens"></div><div class="post-date">18<small>JULY<br>2017</small></div></div>
  <h4>Lorem ipsum dolor sit amet, consectetuer adipiscing elit, sed diam nonummy.</h4>
  <div class="meta"><span><i></i>Dr. Mara Kessel</span>/<span><i></i>0 Comments</span></div>
  <p>Lorem ipsum dolor sit amet, consectetuer adipiscing elit, sed diam nonummy nibh euismod...[+]</p>
</article>
<article class="abs post" style="left:443px">
  <div style="position:relative"><div class="post-img" style="background:linear-gradient(150deg,#4b6a8e,#c9c3bb 55%,#3d4a5a)" role="img" aria-label="Network cables plugged into a patch panel"></div><div class="post-date">18<small>JULY<br>2017</small></div></div>
  <h4>Lorem ipsum dolor sit amet, consectetuer adipiscing elit, sed diam nonummy.</h4>
  <div class="meta"><span><i></i>Dr. Mara Kessel</span>/<span><i></i>0 Comments</span></div>
  <p>Lorem ipsum dolor sit amet, consectetuer adipiscing elit, sed diam nonummy nibh euismod...[+]</p>
</article>
<article class="abs post" style="left:785px">
  <div style="position:relative"><div class="post-img" style="background:linear-gradient(150deg,#cfe0f0,#e8e6e2 50%,#7fa0c0)" role="img" aria-label="Smartphone home automation app in front of a house"></div><div class="post-date">18<small>JULY<br>2017</small></div></div>
  <h4>Lorem ipsum dolor sit amet, consectetuer adipiscing elit, sed diam nonummy.</h4>
  <div class="meta"><span><i></i>Dr. Mara Kessel</span>/<span><i></i>0 Comments</span></div>
  <p>Lorem ipsum dolor sit amet, consectetuer adipiscing elit, sed diam nonummy nibh euismod...[+]</p>
</article>
<svg class="abs side-arrow" style="left:50px" width="16" height="34"><path d="M14 2 3 17l11 15" fill="none" stroke="#ccc" stroke-width="2"/></svg>
<svg class="abs side-arrow" style="left:1134px" width="16" height="34"><path d="M2 2l11 15L2 32" fill="none" stroke="#ccc" stroke-width="2"/></svg>

<!-- send a message -->
<section class="abs message"></section>
<h2 class="abs msg-title">SEND A<br>MESSAGE</h2>
<p class="abs msg-text">Duis autem vel eum iriure dolormi opi inmold hendi rerit in vulpu tatenil velitm essemol mo molestiel conseqh uat, velmi illum dolor eokf no atn nulla more facilisis...[+]</p>
<div class="abs form-label">Please fill up bellow form</div>
<div class="abs field" style="left:458px;top:3243px">Name</div>
<div class="abs field" style="left:793px;top:3243px">Email</div>
<div class="abs field" style="left:458px;top:3294px">Phone</div>
<div class="abs field" style="left:793px;top:3294px">Message</div>
<div class="abs submit">SUBMIT</div>

<!-- footer -->
<footer class="abs footer"></footer>
<div class="abs foot-line" style="left:335px;width:225px"></div>
<div class="abs foot-line" style="left:640px;width:225px"></div>
<div class="abs contact-item" style="left:149px">
  <svg width="20" height="26" viewBox="0 0 20 26"><path d="M10 1a8 8 0 0 0-8 8c0 6 8 15 8 15s8-9 8-15a8 8 0 0 0-8-8z" fill="none" stroke="#999" stroke-width="1.5"/><circle cx="10" cy="9" r="3" fill="#999"/></svg>
  27 Lindenweg, Feldkirch, Austria
</div>
<div class="abs contact-item" style="left:440px">
  <svg width="24" height="26" viewBox="0 0 24 24"><path d="M6.6 10.8a15 15 0 0 0 6.6 6.6l2.2-2.2c.3-.3.7-.4 1-.2 1.1.4 2.3.6 3.6.6.6 0 1 .4 1 1V20c0 .6-.4 1-1 1A17 17 0 0 1 3 4c0-.6.4-1 1-1h3.5c.6 0 1 .4 1 1 0 1.3.2 2.5.6 3.6.1.3 0 .7-.2 1z" fill="none" stroke="#999" stroke-width="1.5"/></svg>
  Phone: 555-014-2270
</div>
<div class="abs contact-item" style="left:731px">
  <svg width="24" height="26" viewBox="0 0 24 24"><path d="M22 2 2 10l8 3 3 9z M10 13 22 2" fill="none" stroke="#999" stroke-width="1.5" stroke-linejoin="round"/></svg>
  Email: info@veltranostrom.com
</div>
<p class="abs foot-text">Lorem ipsum dolor sit amet, consectetuer adipiscing elit, sed diam nonummy nibh euismod tincidunt ut laoreet dolore magna aliquam</p>
<div class="abs foot-btn">CONTACT US</div>

<div class="abs copyright">Copyright © 2017 Veltrano Strom. All Right Reserved.</div>
<div class="abs social" style="left:964px;background:var(--social-1)" role="img" aria-label="Social profile link"></div>
<div class="abs social" style="left:1012px;background:var(--social-2)" role="img" aria-label="Social profile link"></div>
<div class="abs social" style="left:1060px;background:var(--social-3)" role="img" aria-label="Social profile link veltrano_strom"></div>

</body>
</html>
```